Brochure Design Project

We require a great design for a brochure that we will be giving to people who are interested in buying one of our franchises.
From this brochure they will need to get the feel of a succesful business that they would love to be a part of

Please also include the title
Become Part of a National Sign Manufacturing Company

Hi Everyone
Does anyone have any designs that they are adding because we will be making our descision in approx an hour

Thank you

Industry/Entity Type

Business

Requirements
Must have
• This brochure must be 2 page A4 (front and back)
can be either portrait or landscape orientation (which ever works best with the design)
Must have our logo and colours
Must include all the information provided in the Word Document
Nice to have
• Can include images if it works with the design
can use either stock images of profesionals or see our website
www.vorlix.com.au for some images

```html
<!DOCTYPE html>
<html lang="en">
<head>
<meta charset="utf-8">
<title>Become Part of a National Sign Manufacturing Company</title>
<link rel="stylesheet" href="https://fonts.googleapis.com/css2?family=PT+Sans+Narrow:wght@400;700&family=Source+Sans+3:wght@400;600;700&display=swap">
<style>
  :root {
    --backdrop: #a8a9ad;
    --navy: #2b3590;
    --navy-deep: #28347f;
    --royal: #1f6fc0;
    --title-blue: #2a3b94;
    --sub-blue: #2676c4;
    --sky: #92c6f1;
    --white: #ffffff;
    --grey-text: #6a6c70;
    --body-navy: #2a3b8a;
  }
  * { margin: 0; padding: 0; box-sizing: border-box; }
  html, body { width: 1200px; height: 836px; overflow: hidden; }
  body { background: var(--backdrop); position: relative; font-family: "PT Sans Narrow", "Arial Narrow", sans-serif; }
  .page { position: absolute; top: 44px; width: 532px; height: 751px; background: var(--white); box-shadow: 4px 6px 10px rgba(0,0,0,.35); overflow: hidden; }
  .page--front { left: 53px; }
  .page--back { left: 614px; }
  .abs { position: absolute; }
  h2 { font-family: "Source Sans 3", sans-serif; font-weight: 600; }

  /* front */
  .hero-photo { left: 0; top: 0; width: 532px; height: 358px; background: linear-gradient(180deg, #e7eef7 0%, #d8e3ef 50%, #c6d2df 100%); }
  .hero-title { right: 27px; top: 26px; text-align: center; font-family: "Source Sans 3", sans-serif; }
  .hero-title .main { color: var(--title-blue); font-size: 40px; font-weight: 600; line-height: 42px; letter-spacing: -0.5px; }
  .hero-title .sub { color: var(--sub-blue); font-size: 23px; line-height: 28px; }
  .col-opportunity { left: 0; top: 358px; width: 192px; height: 293px; background: var(--navy); color: var(--white); padding: 16px 14px 0 28px; }
  .col-benefits { left: 192px; top: 358px; width: 340px; height: 293px; background: var(--royal); color: var(--white); padding: 16px 22px 0 13px; }
  .col-opportunity h2, .col-benefits h2 { font-size: 21px; margin-bottom: 10px; }
  .col-opportunity p { font-size: 12px; line-height: 13.6px; text-align: justify; }
  .benefit-list { list-style: none; font-size: 12px; line-height: 13.6px; }
  .benefit-list li { padding-left: 7px; text-indent: -5px; }
  .benefit-list li::before { content: "•"; margin-right: 2px; }
  .notch { left: 392px; top: 650px; }
  .brand { left: 29px; top: 668px; font-family: "Source Sans 3", sans-serif; font-weight: 700; font-size: 23px; color: var(--navy); letter-spacing: 1px; }
  .cta { left: 29px; top: 696px; font-family: "Source Sans 3", sans-serif; font-weight: 600; font-size: 15.5px; color: var(--grey-text); }
  .contacts { left: 29px; top: 720px; display: flex; gap: 18px; font-family: "Source Sans 3", sans-serif; font-weight: 600; font-size: 15px; color: var(--grey-text); align-items: center; }
  .contacts span { display: flex; align-items: center; gap: 5px; }

  /* back */
  .clients-col { left: 0; top: 0; width: 316px; height: 751px; background: var(--navy); color: var(--white); padding: 20px 20px 0 28px; }
  .clients-col h2.lead { font-size: 21px; margin-bottom: 4px; }
  .clients-col h3 { font-family: "Source Sans 3", sans-serif; font-weight: 600; font-size: 16px; margin-top: 10px; line-height: 18px; }
  .clients-col p { font-size: 11.6px; line-height: 12.6px; text-align: justify; }
  .site-photo { left: 316px; top: 0; width: 216px; height: 214px; background: linear-gradient(160deg, #e9f0f8 0%, #c9d9ea 45%, #b4c88a 100%); }
  .pointer { left: 316px; top: 134px; }
  .needs-col { left: 316px; top: 214px; width: 216px; height: 440px; background: var(--sky); color: var(--body-navy); padding: 10px 20px 0 18px; }
  .needs-col h2 { font-size: 20px; color: var(--navy); margin-bottom: 8px; }
  .needs-col p { font-size: 11.6px; line-height: 12.6px; text-align: justify; margin-bottom: 12px; }
  .costs { left: 316px; top: 654px; width: 216px; height: 84px; background: var(--white); padding: 10px 18px; color: var(--body-navy); }
  .costs h2 { font-size: 16px; color: var(--navy); margin-bottom: 10px; }
  .costs ul { list-style: none; font-size: 11.6px; line-height: 12.6px; }
  .costs li::before { content: "• "; }
  .costs-bar { left: 334px; top: 738px; width: 180px; height: 13px; background: var(--navy); }
</style>
</head>
<body>

<section class="page page--front">
  <div class="abs hero-photo" role="img" aria-label="Smiling businessman in a suit holding a laptop, with colleagues meeting at a desk in a bright office behind him"></div>
  <div class="abs hero-title">
    <div class="main">BECOME PART OF</div>
    <div class="sub">A NATIONAL SIGN</div>
    <div class="sub">MANUFACTURING COMPANY</div>
  </div>

  <div class="abs col-opportunity">
    <h2>OPPORTUNITY</h2>
    <p>An exciting opportunity exists for 7 people to become part of a national sign manufacturing company servicing big name clientele on a national scale. A successful applicant will receive their own State territory branch to operate a sign manufacturing and installation service to our existing clientele. This will be strictly limited to 1 franchise sold per state and if the operator chooses or feels they can better service our clients with multiple outlets within their state then they are at liberty to do so without any further fees incurred.</p>
  </div>

  <div class="abs col-benefits">
    <h2>WHAT DO YOU GET</h2>
    <ul class="benefit-list">
      <li>You will receive your own State to operate and fulfil all orders within that state</li>
      <li>You can have as many manufacturing facilities you feel are needed to efficiently operate within your state and the best part is that you can grow this over time.</li>
      <li>Operating Procedures and software including quoting systems and pricing structure</li>
      <li>Pre-existing clientele we have been operating since 2006 and have a national network that is growing by the day</li>
      <li>National website and number</li>
      <li>Marketing and new client introduction</li>
      <li>Benefits of being part of a national team that is capable of servicing national clients that would not be possible to service otherwise</li>
      <li>The benefits of this business are growing daily and we have not even scratched the surface of its full potential more and more clients are realising just how much they can benefit from using our services.</li>
    </ul>
  </div>

  <svg class="abs notch" width="86" height="46" viewBox="0 0 86 46"><polygon points="0,0 86,0 43,46" fill="#1f6fc0"/></svg>

  <div class="abs brand">VORLIX</div>
  <div class="abs cta">FOR MORE INFORMATION OR TO APPLY CALL</div>
  <div class="abs contacts">
    <span><svg width="17" height="15" viewBox="0 0 17 15"><polygon points="8.5,0 17,7.5 14.5,7.5 14.5,15 10.5,15 10.5,10 6.5,10 6.5,15 2.5,15 2.5,7.5 0,7.5" fill="#1f6fc0"/></svg>www.vorlix.com.au</span>
    <span><svg width="15" height="15" viewBox="0 0 24 24"><path d="M6.6 10.8a15.1 15.1 0 0 0 6.6 6.6l2.2-2.2a1 1 0 0 1 1-.25 11.4 11.4 0 0 0 3.6.57 1 1 0 0 1 1 1V20a1 1 0 0 1-1 1A17 17 0 0 1 3 4a1 1 0 0 1 1-1h3.5a1 1 0 0 1 1 1c0 1.25.2 2.45.57 3.57a1 1 0 0 1-.25 1z" fill="#1f6fc0"/></svg>1300 555 019</span>
    <span><svg width="17" height="13" viewBox="0 0 17 13"><rect x="0.5" y="0.5" width="16" height="12" fill="#1f6fc0"/><polyline points="1,1 8.5,7.5 16,1" fill="none" stroke="#fff" stroke-width="1.4"/></svg>accounts@vorlix.com.au</span>
  </div>
</section>

<section class="page page--back">
  <div class="abs clients-col">
    <h2 class="lead">OUR CLIENTS</h2>
    <p>Our clients are franchises, shopfitters, architects, designers, brokers, multisite organisations and anyone who is ordering signs on a regular basis. We have targeted this clientele for the obvious reasons of continuous work and in return our clients receive:</p>

    <h3>Competitive Pricing</h3>
    <p>The reason you will be able to offer competitive pricing is because you will not have to waste time and money on things like in-house design, advertising, sales reps high exposure sales locations and the list goes on<br>All of these savings are passed on to our clients and for this reason we remain number 1 choice time and time again.</p>

    <h3>Consistency and Reliability</h3>
    <p>We have systems in place to ensure consistency and reliability across branches by adhering to a minimum standards and code of conduct policy which our customers can view at any time which outlines things such as standard material specifications, warranty periods, standard turnaround times, standard pricing schedules and more, to add to all this the operating systems and software we use ensure reliable and familiar interaction with our clients no matter which branch they are dealing with.</p>

    <h3>Ease of Use</h3>
    <p>Just think about it one of the roles of an operations manager of a large company is the organisation and ordering all of the signage requirements for 45 different locations across Australia. Whilst at one of the locations in NSW he notices that the front window graphics have been damaged by graffiti, He calls the NSW Vorlix branch and begins the process of ordering some replacement window graphics and chooses to freshen up the graphics with some new designs that had been recently added to the brands new style guide, now he already knows that he is getting a quality product that has been specified in the minimum standards and code of conduct policy and he already knows the cost of the product because the pricing structure has also been outlined he knows that the branch has access to the customers data base with style guide so he knows they have the artwork files plus he knows that the colours will be correct because all that info is in the customers file, so in other words he know how easy it is to order from the Vorlix branch. Then one week later he is in Victoria visiting another one of the 45 locations and would you believe he notices that yet again the windows have been vandalised and yes another opportunity to refresh the images so off course he call the Vorlix VIC office and begins the process again and all he has to do is say we want the graphics exactly the same as the ones done 2 weeks ago at the other location, Easy</p>
  </div>

  <div class="abs site-photo" role="img" aria-label="Two workers in hard hats and high-visibility vests inspecting a glass roof structure"></div>
  <svg class="abs pointer" width="34" height="58" viewBox="0 0 34 58"><polygon points="0,0 34,29 0,58" fill="#2b3590"/></svg>

  <div class="abs needs-col">
    <h2>WHAT YOU NEED</h2>
    <p>To be successful in ensuring your position within our team you will need to have had experience within the signage industry, have great communication skills and have a good positive attitude towards owning and running a successful business. Under no circumstances can you own or be in any way affiliated with another sign company and own a Vorlix branch you can however apply if you are closing or exiting (or intending to exit if successful)</p>
    <p>Some working capital will be needed and this will obviously vary depending on the size of the initial manufacturing setup but a minimum of $20,000 would be advised.</p>
    <p>A Once off purchase price of your territory will cost $45,000.</p>
    <p>A suitable place of business, at a minimum this will consist of small office area and ideally 200sqm or more of workshop space.</p>
    <p>There is various machinery and equipment required and leasing options will be available</p>
  </div>

  <div class="abs costs">
    <h2>Costs</h2>
    <ul>
      <li>$45,000 once off purchase price for your territory</li>
      <li>7% of sales</li>
    </ul>
  </div>
  <div class="abs costs-bar"></div>
</section>

</body>
</html>
```